Managed Service Provider VOIP Flyer

Looking for a one page US letter size single or double sided brochure to offer cloud hosted VoIP Phone system and unified communications. We have partnered with a VoIP Phone system company and want to sell their services but we don't want their name to be shown on the brochure because customers might call them directly. The company name is Quorvel (www.quorvel-example.com) and our company name is Lumen By Harlow, LLC and our voice product is called Clearly Talk. I have also uploaded my company's logo that you should show on the brochure and use that coloring. For more details about the product, you can visit their website mentioned above. Also I am looking for something very similar to this project and many of the technical details are the same https://flyer.contestpad-example.com/contest/5817264

I have also uploaded a PDF with my different package levels and some of the included features. Depending on the design we may or may not want the package levels on this flyer.

Target Market(s)

Small and medium Businesses

Industry/Entity Type

Voip

Requirements
Must have
• Feature and benefits information of Managed VOICE. Use my logo and coloring from my logo. Include our website, email, phone and possibly facebook if it makes sense/looks good.

www.lumenbyharlow-example.com
415.836.0.917
sales@lumenbyharlow-example.com
www.socialsite-example.com/lumenbyharlow
Nice to have
• Would like to show how the service is simple and reliable and available for any business size

```html
<!DOCTYPE html>
<html lang="en">
<head>
<meta charset="utf-8">
<title>Lumen By Harlow – IT Consulting &amp; Services</title>
<link href="https://fonts.googleapis.com/css2?family=Josefin+Sans:ital,wght@0,400;0,600;0,700;1,700&display=swap" rel="stylesheet">
<style>
  :root{
    --navy:#1f3a78;
    --navy-deep:#142a5c;
    --red:#c4262e;
    --paper:#f4f3f7;
    --band:#e3e3ea;
    --backdrop:#d9d9de;
    --grey-head:#8d8c92;
    --rule:#c9c8ce;
    --ink:#3c3c44;
    --body-ink:#2b3350;
    --muted:#8a8a92;
    --photo-a:#0d1e3c;
    --photo-b:#2a5a86;
  }
  *{margin:0;padding:0;box-sizing:border-box}
  html,body{width:900px;height:1200px;overflow:hidden;background:var(--backdrop)}
  body{font-family:"Josefin Sans",sans-serif;color:var(--ink);position:relative}

  /* Each side is built at 900×1200 and shown at half size, front above back */
  .sheet{position:absolute;left:225px;width:900px;height:1200px;background:var(--paper);transform:scale(.5);transform-origin:0 0;overflow:hidden}
  .sheet-front{top:0}
  .sheet-back{top:600px}

  .shapes{position:absolute;left:0;top:0}

  /* Front */
  .brand{position:absolute;left:48px;top:70px;display:flex;align-items:center;gap:14px}
  .brand-mark{width:40px;height:40px;background:var(--red)}
  .brand-name{font-weight:700;font-size:30px;letter-spacing:1px;color:var(--navy);line-height:1}
  .headline{position:absolute;left:48px;top:222px;color:#fff;font-weight:700;font-size:38px;line-height:1.1;letter-spacing:1.5px;text-transform:uppercase}
  .pricing{position:absolute;left:40px;top:340px;width:820px;border-collapse:collapse;font-size:14px;border:1px solid var(--rule)}
  .pricing th{background:var(--grey-head);color:#fff;font-weight:600;height:60px;font-size:15px;line-height:1.15}
  .pricing th small{display:block;font-weight:400;font-size:11px;opacity:.9}
  .pricing td{height:28px;border-bottom:1px solid var(--rule);padding:0 12px;vertical-align:middle}
  .pricing td.feature{width:340px}
  .pricing td.val{width:160px;text-align:center;border-left:1px solid var(--rule)}
  .pricing td.no{color:var(--muted)}
  .pricing tr.price td.val{font-weight:700}
  .pricing tr.tall td{height:40px;line-height:1.15}

  /* Footer (both sides) */
  .company{position:absolute;left:34px;top:1150px;color:#fff;font-size:17px;font-weight:600;white-space:nowrap}
  .contacts{position:absolute;left:358px;top:1130px;width:522px;display:flex;justify-content:space-between;color:#fff;font-size:11.5px;align-items:center;white-space:nowrap}
  .contacts span{display:flex;align-items:center;gap:6px}
  .contacts svg{flex:none}

  /* Back */
  .features{position:absolute;left:0;width:900px;padding:0 40px}
  .features-seat{top:46px}
  .features-pbx{top:600px;height:300px;padding-top:14px;background:linear-gradient(180deg,var(--band),var(--paper))}
  .features-addon{top:905px}
  .section-title{display:flex;align-items:center;margin-bottom:16px}
  .section-tag{background:var(--red);color:#fff;font-weight:700;font-size:16px;padding:7px 16px 5px;white-space:nowrap}
  .section-tag.caps{text-transform:uppercase;letter-spacing:1px}
  .section-rule{flex:1;height:2px;background:var(--red)}
  .section-rule.lead{flex:0 0 220px}
  .columns{display:grid;grid-template-columns:1fr 1fr;column-gap:40px}
  .feature-item{margin-bottom:9px}
  .feature-item h3{font-weight:700;font-style:italic;font-size:16px;color:var(--navy);line-height:1.25}
  .feature-item p{font-size:13px;line-height:1.3;color:var(--body-ink)}
</style>
</head>
<body>

<section class="sheet sheet-front">
  <svg class="shapes" width="900" height="1200" viewBox="0 0 900 1200">
    <defs>
      <linearGradient id="techGlow" x1="0" y1="0" x2="1" y2="1">
        <stop offset="0" stop-color="#2a5a86"/>
        <stop offset="1" stop-color="#0d1e3c"/>
      </linearGradient>
    </defs>
    <polygon points="440,0 900,0 900,320 540,320 480,200" fill="url(#techGlow)" role="img" aria-label="Photo of a hand holding a glowing digital lock surrounded by cloud and communication icons"/>
    <polygon points="0,200 480,200 540,320 0,320" fill="#1f3a78"/>
    <polyline points="440,0 480,200 540,320" fill="none" stroke="#c4262e" stroke-width="5"/>
    <line x1="0" y1="200" x2="480" y2="200" stroke="#c4262e" stroke-width="4"/>
    <polygon points="0,1130 320,1130 290,1200 0,1200" fill="#1f3a78"/>
    <polygon points="345,1108 900,1108 900,1170 318,1170" fill="#c4262e"/>
    <polygon points="300,1178 900,1178 900,1200 290,1200" fill="#1f3a78"/>
  </svg>

  <div class="brand"><div class="brand-mark"></div><div class="brand-name">LUMEN BY HARLOW</div></div>
  <div class="headline">IT Consulting<br>&amp; Services</div>

  <table class="pricing">
    <thead>
      <tr><th></th><th>Primer<small>(Location, not a user)</small></th><th>Standard<small>(Basic user)</small></th><th>Premium<small>(Power user)</small></th></tr>
    </thead>
    <tbody>
      <tr class="price"><td class="feature">Monthly Price</td><td class="val">$20</td><td class="val">$30</td><td class="val">$35</td></tr>
      <tr><td class="feature">Extension Dialing</td><td class="val">Yes</td><td class="val">Yes</td><td class="val">Yes</td></tr>
      <tr><td class="feature">Local Outbound Calls Only</td><td class="val">Yes</td><td class="val">LD Included</td><td class="val">LD Included</td></tr>
      <tr><td class="feature">Caller ID and Caller Name Delivery</td><td class="val">Yes</td><td class="val">Yes</td><td class="val">Yes</td></tr>
      <tr><td class="feature">Call Logs</td><td class="val">Yes</td><td class="val">Yes</td><td class="val">Yes</td></tr>
      <tr><td class="feature">Last Number Redial</td><td class="val">Yes (Local Only)</td><td class="val">Yes</td><td class="val">Yes</td></tr>
      <tr><td class="feature">Music On Hold</td><td class="val">Yes</td><td class="val">Yes</td><td class="val">Yes</td></tr>
      <tr><td class="feature">Corporate Directory Access</td><td class="val">Yes</td><td class="val">Yes</td><td class="val">Yes</td></tr>
      <tr><td class="feature">E911 Service</td><td class="val">Yes</td><td class="val">Yes</td><td class="val">Yes</td></tr>
      <tr><td class="feature">Call Park</td><td class="val no">No</td><td class="val">Yes</td><td class="val">Yes</td></tr>
      <tr class="tall"><td class="feature">Call Forwarding (Always, Busy,<br>No-Answer, Not Reachable)</td><td class="val no">No</td><td class="val">Yes</td><td class="val">Yes</td></tr>
      <tr><td class="feature">Call Recording</td><td class="val no">No</td><td class="val">Additional</td><td class="val">Additional</td></tr>
      <tr><td class="feature">Call Transfer</td><td class="val no">No</td><td class="val">Yes</td><td class="val">Yes</td></tr>
      <tr><td class="feature">Call Waiting</td><td class="val no">No</td><td class="val">Yes</td><td class="val">Yes</td></tr>
      <tr><td class="feature">Unified Messaging</td><td class="val no">No</td><td class="val">Yes</td><td class="val">Yes</td></tr>
      <tr><td class="feature">Inclusion in Hunt Groups</td><td class="val no">No</td><td class="val">Yes</td><td class="val">Yes</td></tr>
      <tr><td class="feature">Simultaneous Ring</td><td class="val no">No</td><td class="val">Yes</td><td class="val">Yes</td></tr>
      <tr><td class="feature">Sequential Ring</td><td class="val no">No</td><td class="val">Yes</td><td class="val">Yes</td></tr>
      <tr><td class="feature">Speed Dial 100</td><td class="val no">No</td><td class="val">Yes</td><td class="val">Yes</td></tr>
      <tr><td class="feature">Three-Way Calling</td><td class="val no">No</td><td class="val">Yes</td><td class="val">Yes</td></tr>
      <tr><td class="feature">Deskline Client</td><td class="val no">No</td><td class="val no">No</td><td class="val">Yes</td></tr>
      <tr><td class="feature">Desktop Sharing</td><td class="val no">No</td><td class="val no">No</td><td class="val">Yes</td></tr>
      <tr><td class="feature">Web Collaboration</td><td class="val no">No</td><td class="val no">No</td><td class="val">Yes</td></tr>
    </tbody>
  </table>

  <div class="company">Lumen By Harlow, LLC</div>
  <div class="contacts">
    <span><svg width="14" height="14" viewBox="0 0 24 24"><path fill="#fff" d="M6.6 10.8a15 15 0 0 0 6.6 6.6l2.2-2.2a1 1 0 0 1 1-.25 11.4 11.4 0 0 0 3.6.57 1 1 0 0 1 1 1V20a1 1 0 0 1-1 1A17 17 0 0 1 3 4a1 1 0 0 1 1-1h3.5a1 1 0 0 1 1 1c0 1.25.2 2.45.57 3.57a1 1 0 0 1-.25 1z"/></svg>+1 (415) 836-0917</span>
    <span><svg width="14" height="14" viewBox="0 0 24 24"><rect x="2" y="5" width="20" height="14" rx="2" fill="none" stroke="#fff" stroke-width="2"/><path d="M2 6l10 7 10-7" fill="none" stroke="#fff" stroke-width="2"/></svg>sales@lumenbyharlow-example.com</span>
    <span><svg width="14" height="14" viewBox="0 0 24 24"><circle cx="12" cy="12" r="9.5" fill="none" stroke="#fff" stroke-width="2"/><path d="M2.5 12h19M12 2.5c3 3 3 16 0 19M12 2.5c-3 3-3 16 0 19" fill="none" stroke="#fff" stroke-width="1.6"/></svg>www.lumenbyharlow-example.com</span>
  </div>
</section>

<section class="sheet sheet-back">
  <div class="features features-seat">
    <div class="section-title"><div class="section-rule lead"></div><div class="section-tag caps">Seat Features:</div><div class="section-rule"></div></div>
    <div class="columns">
      <div>
        <div class="feature-item"><h3>3-Way Calling</h3><p>With a 3-Way Call, or an ad-hoc conference, you can bring two other lines (internal and/or external) into a call with you.</p></div>
        <div class="feature-item"><h3>Call Logs</h3><p>Your administrator will have access to view call detail records, such as inbound and outbound calls, time, and duration.</p></div>
        <div class="feature-item"><h3>Caller ID and Caller Name Delivery</h3><p>Incoming calls will include the incoming caller ID and caller name if provided by the network.</p></div>
        <div class="feature-item"><h3>Call Waiting</h3><p>Call waiting allows you to receive a new call while you are still on an existing call.</p></div>
        <div class="feature-item"><h3>Call Forward Always</h3><p>Forward all incoming calls to another extension or phone number.</p></div>
        <div class="feature-item"><h3>Call Forward Busy</h3><p>Forward incoming calls to another extension or phone number when your phone is busy or in Do Not Disturb mode.</p></div>
        <div class="feature-item"><h3>Call Forward No Answer</h3><p>Forward unanswered calls to an extension or phone number other than the voicemail after a set number of rings (default 3).</p></div>
        <div class="feature-item"><h3>Call Forward Not Reachable</h3><p>In the event that you lose your internet service, you can set a number to forward calls to when your phone is offline.</p></div>
      </div>
      <div>
        <div class="feature-item"><h3>Do Not Disturb</h3><p>Placing your phone service in Do Not Disturb will cause all calls to go to your voicemail box or specified busy treatment.</p></div>
        <div class="feature-item"><h3>Extension Dialing</h3><p>You may call other phones in your PBX with an extension, even if they are in other locations.</p></div>
        <div class="feature-item"><h3>Sequential Ring</h3><p>A sequence of extensions and numbers can be set up to dial if the desk phone does not pick up.</p></div>
        <div class="feature-item"><h3>Simultaneous Ring</h3><p>You can specify extensions and numbers to ring at the same time as the desk line extension.</p></div>
        <div class="feature-item"><h3>Last Number Redial</h3><p>You can redial the last number you called.</p></div>
        <div class="feature-item"><h3>Speed Dial 100</h3><p>You can specify up to 100 number to dial with #xx with the dial pad.</p></div>
        <div class="feature-item"><h3>Unified Messaging</h3><p>Your seat has voicemail included, but can also be configured for voicemail to email, zero-out, and email notifications.</p></div>
      </div>
    </div>
  </div>

  <div class="features features-pbx">
    <div class="section-title"><div class="section-rule lead"></div><div class="section-tag">All PBX Include the Following Features:</div><div class="section-rule"></div></div>
    <div class="columns">
      <div>
        <div class="feature-item"><h3>Auto Attendant</h3><p>An automated recording that answers the phone and provides a personalized message to callers with options for connecting to the operator, dialing by name or extension, or connecting to up to nine configurable extensions. Configuration via the Customer Portal allows for hours of operation to be modified, with different options available for hours that the company is open or closed.</p></div>
        <div class="feature-item"><h3>Hunt Groups</h3><p>Allows users within a group to be included in a specified sub-group to handle incoming calls received by an assigned Hunt Group’s phone number. Within the Customer Portal, company administrators can choose from ‘hunt’ schemes, each of which rings the specified phones in a different manner.</p></div>
      </div>
      <div>
        <div class="feature-item"><h3>Corporate Directory</h3><p>System Users are networked for extension to extension calling.</p></div>
        <div class="feature-item"><h3>Company Main Number</h3><p>Phone number with unlimited incoming minutes that can be configured to point to any group extension in the PBX (such as an auto attendant or hunt group).</p></div>
        <div class="feature-item"><h3>Music on Hold</h3><p>Enables company administrators to upload an audio file (wav file containing music, advertising, etc.) onto the system to be broadcast to parties while on hold.</p></div>
      </div>
    </div>
  </div>

  <div class="features features-addon">
    <div class="section-title"><div class="section-rule lead"></div><div class="section-tag">Add-On Features:</div><div class="section-rule"></div></div>
    <div class="columns">
      <div>
        <div class="feature-item"><h3>Advanced Auto Attendant</h3><p>A multi-level Auto Attendant (for example, enterprise’s main Auto Attendant is configured to seamlessly route to the Auto Attendant of a particular department or location).</p></div>
        <div class="feature-item"><h3>Toll-Free Numbers</h3><p>An “800” number with inbound calling charged a toll to you, not the caller.</p></div>
      </div>
      <div>
        <div class="feature-item"><h3>Call Recording</h3><p>Allows a user to record their calls in either an always on or on-demand mode. These recording capabilities can allow for personal monitoring or supervised monitoring of recorded calls.</p></div>
        <div class="feature-item"><h3>Virtual Number</h3><p>Additional phone number with unlimited incoming minutes that can be configured to point to any extension in the PBX.</p></div>
      </div>
    </div>
  </div>

  <svg class="shapes" width="900" height="1200" viewBox="0 0 900 1200">
    <polygon points="0,1130 320,1130 290,1200 0,1200" fill="#1f3a78"/>
    <polygon points="345,1108 900,1108 900,1170 318,1170" fill="#c4262e"/>
    <polygon points="300,1178 900,1178 900,1200 290,1200" fill="#1f3a78"/>
  </svg>
  <div class="company">Lumen By Harlow, LLC</div>
  <div class="contacts">
    <span><svg width="14" height="14" viewBox="0 0 24 24"><path fill="#fff" d="M6.6 10.8a15 15 0 0 0 6.6 6.6l2.2-2.2a1 1 0 0 1 1-.25 11.4 11.4 0 0 0 3.6.57 1 1 0 0 1 1 1V20a1 1 0 0 1-1 1A17 17 0 0 1 3 4a1 1 0 0 1 1-1h3.5a1 1 0 0 1 1 1c0 1.25.2 2.45.57 3.57a1 1 0 0 1-.25 1z"/></svg>+1 (415) 836-0917</span>
    <span><svg width="14" height="14" viewBox="0 0 24 24"><rect x="2" y="5" width="20" height="14" rx="2" fill="none" stroke="#fff" stroke-width="2"/><path d="M2 6l10 7 10-7" fill="none" stroke="#fff" stroke-width="2"/></svg>sales@lumenbyharlow-example.com</span>
    <span><svg width="14" height="14" viewBox="0 0 24 24"><circle cx="12" cy="12" r="9.5" fill="none" stroke="#fff" stroke-width="2"/><path d="M2.5 12h19M12 2.5c3 3 3 16 0 19M12 2.5c-3 3-3 16 0 19" fill="none" stroke="#fff" stroke-width="1.6"/></svg>www.lumenbyharlow-example.com</span>
  </div>
</section>

</body>
</html>
```